Proposal Document Template for New Accounting and Tax Clients

Hi Tarek,
We hope you are well.
We are an Accounting Firm based in the suburb of Pyrmont near Sydney city, and you recently designed a Package Title page for us that we use when providing our clients their year end statements and tax returns.

Because we like the design so much, we would like to work with you again. We would like you to incorporate aspects of your original Package Title Page design throughout our Proposal Document to provide design consistency between both documents.

We need our Proposal Document to be a fully editable Word document, as we send it to potential new clients to win their business and we will need to adjust what we include to suit each one.

We also think it could work if the design includes key images from our website.

We have two key brand colours:
Blue - Hex code #021738
Gold - Hex code #b2a98c

I have included:
- New Thornvale Advisory Title Page_050225 - this was your previous design that we would like the Proposal Document to look similar to
- Proposal Document_V2_Detailed_Owen - this is our current Proposal Document that we would like you to redesign, keeping the content, but updating the design to look consistent with the New Thornvale Advisory Title Page.
- Our Logo in different colours in JPEG Format (I also have PNG and EPS files of these. If you need them, please let me know)
- The key images from our website www.thornvale.net.au

Please let me know if you have any questions or need anything further.

Thank you in advance
Jo
Updates

We received the designs one day ago, that combined with the Easter Holiday break means we need more time to review and provide feedback.

Target Market(s)

Accounting, Tax, and Strategic Business Planning Clients from Small Business, to Corporates , and Individuals

Industry/Entity Type

Accounting

Font styles to use
Other font styles liked:
• Calibri

Requirements
Must have
• Our logo and the ability to edit the document
Nice to have
• Include images from our website thornvale.net.au

```html
<!DOCTYPE html>
<html lang="en">
<head>
<meta charset="utf-8">
<title>Thornvale Advisory – Services Proposal 2025</title>
<link href="https://fonts.googleapis.com/css2?family=Carlito:wght@400;700&family=Montserrat:wght@300;400;600&display=swap" rel="stylesheet">
<style>
  :root{
    --navy:#021738;
    --navy-2:#0c2a55;
    --gold:#b2a98c;
    --gold-soft:#d9d3c0;
    --paper:#ffffff;
    --ink:#2b2f36;
    --muted:#6b7078;
    --panel:#eef0f3;
    --stage:#ececec;
  }
  *{box-sizing:border-box;margin:0;padding:0}
  html,body{width:1200px;height:3236px;overflow:hidden}
  body{background:var(--stage);font-family:"Carlito",Calibri,sans-serif;color:var(--ink);position:relative}
  .heading{font-family:"Montserrat",sans-serif}

  /* ---------- cover ---------- */
  .cover{position:absolute;left:300px;top:60px;width:600px;height:848px;background:var(--navy);overflow:hidden}
  .cover-art{position:absolute;inset:0}
  .logo{position:absolute;font-family:"Carlito",Calibri,sans-serif;font-weight:400;line-height:1;letter-spacing:.5px}
  .cover .logo{left:44px;top:40px;color:#fff;font-size:26px}
  .cover .logo span{display:block;font-size:26px}
  .cover-title{position:absolute;left:44px;top:620px;color:var(--gold);font-family:"Montserrat",sans-serif;font-weight:400;font-size:40px;line-height:1.08;letter-spacing:1px}
  .cover-year{position:absolute;right:44px;top:672px;color:#fff;font-family:"Montserrat",sans-serif;font-weight:600;font-size:34px}
  .cover-date{position:absolute;left:44px;top:728px;color:var(--gold);font-size:14px;letter-spacing:2px}
  .cover-contact{position:absolute;left:300px;top:756px;width:260px;color:#c9cfdb;font-size:10px;line-height:1.45}

  /* ---------- spreads ---------- */
  .spread{position:absolute;left:155px;width:890px;height:630px;display:flex}
  .spread-1{top:1010px}
  .spread-2{top:1760px}
  .spread-3{top:2510px}
  .page{position:relative;width:445px;height:630px;background:var(--paper);overflow:hidden}
  .page + .page{border-left:1px solid #dcdcdc}
  .page-bar{position:absolute;left:0;right:0;top:0;height:12px;background:var(--navy);border-bottom:3px solid var(--gold)}
  .photo{position:absolute}
  .body-text{position:absolute;font-size:7.2px;line-height:1.5;color:var(--ink)}
  .body-text p{margin-bottom:5px}
  .body-text b{color:var(--navy)}

  /* spread 1 */
  .about-photo{left:0;top:15px;width:200px;height:215px;background:linear-gradient(180deg,#9fb4cc 0%,#c7d3df 45%,#6d7f93 75%,#3b4a5c 100%)}
  .about-heading{position:absolute;left:20px;top:250px;width:170px;text-align:right;color:var(--navy);font-family:"Montserrat",sans-serif;font-weight:400;font-size:19px;line-height:1.15;letter-spacing:.5px}
  .about-text{left:212px;top:40px;width:212px}
  .glass-photo{left:0;top:410px;width:250px;height:220px;background:linear-gradient(135deg,#0b2245 0%,#1f4f8a 40%,#5a87b8 60%,#0d2a52 100%)}
  .glass-strip{left:250px;top:560px;width:195px;height:70px;background:linear-gradient(90deg,#1b3d6b,#7898bd)}
  .team-title{position:absolute;left:28px;top:34px;color:var(--navy);font-family:"Montserrat",sans-serif;font-size:15px;letter-spacing:1px}
  .team-grid{position:absolute;left:150px;top:30px;width:276px;display:grid;grid-template-columns:repeat(4,66px);grid-auto-rows:74px;gap:4px}
  .team-photo{background:linear-gradient(180deg,#d8d8d8,#9b9b9b)}
  .team-card{padding:8px 5px;color:#fff;font-size:6.5px;line-height:1.3}
  .team-card strong{display:block;font-size:7.5px;margin-bottom:2px}
  .team-card.gold{background:var(--gold)}
  .team-card.navy{background:var(--navy)}
  .team-card.blank{background:#f2f2f2}
  .tower-photo{left:120px;top:330px;width:180px;height:270px;background:linear-gradient(90deg,#3c3f44 0%,#8b8f96 30%,#d6d8dc 50%,#6a6e75 75%,#2d3035 100%)}

  /* spread 2 */
  .proposal-heading{position:absolute;left:30px;top:34px;color:var(--navy);font-family:"Montserrat",sans-serif;font-weight:400;font-size:17px;line-height:1.2;letter-spacing:.5px}
  .prepared{left:30px;top:112px;width:380px}
  .bio{position:absolute;left:30px;width:385px;height:150px;background:var(--panel)}
  .bio-1{top:178px}
  .bio-2{top:346px}
  .bio-photo{position:absolute;left:12px;top:14px;width:80px;height:96px;background:linear-gradient(180deg,#cfcfcf,#8c8c8c)}
  .bio-caption{position:absolute;left:12px;top:112px;width:80px;height:26px;background:var(--navy);color:#fff;font-size:6px;padding:4px;line-height:1.25}
  .bio-text{left:106px;top:14px;width:268px}
  .letter .logo{left:30px;top:30px;color:var(--navy);font-size:20px}
  .letter .logo span{display:block}
  .letter-text{left:30px;top:100px;width:385px}

  /* spread 3 */
  .fee-table{position:absolute;left:30px;width:385px;border-collapse:collapse;font-size:7px}
  .fee-table th{background:var(--navy);color:#fff;text-align:left;padding:3px 5px;font-weight:700}
  .fee-table td{padding:3px 5px;border-bottom:1px solid #e3e0d6}
  .fee-table tr:nth-child(even) td{background:#f4f2ec}
  .fee-table .num{text-align:right}
  .fee-table .total td{background:var(--gold-soft);font-weight:700;color:var(--navy)}
  .fees-1{top:30px}
  .fees-2{top:380px}
  .fees-note{left:30px;top:230px;width:385px}
  .fees-tail{left:30px;top:520px;width:385px}
  .close-text{left:30px;top:34px;width:385px}
  .panels{position:absolute;left:60px;top:110px;width:360px;height:500px}
</style>
</head>
<body>

<!-- Cover -->
<section class="cover" aria-label="Services proposal cover">
  <svg class="cover-art" width="600" height="848" viewBox="0 0 600 848">
    <defs>
      <linearGradient id="skyline" x1="0" y1="0" x2="0" y2="1">
        <stop offset="0" stop-color="#5f7fa6"/>
        <stop offset=".45" stop-color="#b9c6d6"/>
        <stop offset=".7" stop-color="#6b7c8e"/>
        <stop offset="1" stop-color="#a9a79d"/>
      </linearGradient>
    </defs>
    <polygon points="0,0 600,0 600,640 0,430" fill="url(#skyline)" role="img" aria-label="Photo of the city skyline across the harbour with a stone foreshore"/>
    <polygon points="0,430 600,640 600,848 0,848" fill="var(--navy)"/>
    <line x1="0" y1="430" x2="600" y2="640" stroke="var(--gold)" stroke-width="4"/>
  </svg>
  <div class="logo">thornvale<span>advisory</span></div>
  <h1 class="cover-title">SERVICES<br>PROPOSAL</h1>
  <div class="cover-year">2025</div>
  <div class="cover-date">7 January 2025</div>
  <div class="cover-contact">Thornvale Advisory Pty Ltd<br>Level 2, 14 Harbour Lane, Pyrmont NSW<br>www.thornvale.net.au</div>
</section>

<!-- Spread 1: About / Team -->
<div class="spread spread-1">
  <section class="page">
    <div class="page-bar"></div>
    <div class="photo about-photo" role="img" aria-label="Photo of city towers under a pale sky"></div>
    <h2 class="about-heading">ABOUT<br>THORNVALE<br>ADVISORY</h2>
    <div class="body-text about-text">
      <p>We are a chartered accounting firm based in Pyrmont, working with small businesses, corporates and individuals across Sydney and beyond.</p>
      <p>For over twenty years our team has helped clients grow, plan and stay compliant, with advice that is clear, timely and practical.</p>
      <p>We provide accounting, tax, strategic planning and outsourced CFO services, tailored to the needs of each client and each stage of their business.</p>
      <p>Our people take the time to understand your goals, so the numbers support the decisions that matter most to you.</p>
    </div>
    <div class="photo glass-photo" role="img" aria-label="Photo of blue glass office facades"></div>
    <div class="photo glass-strip" role="img" aria-label="Photo of glass building detail"></div>
  </section>
  <section class="page">
    <div class="page-bar"></div>
    <h2 class="team-title">OUR TEAM</h2>
    <div class="team-grid">
      <div class="team-photo" role="img" aria-label="Portrait of a director"></div>
      <div class="team-card navy"><strong>Owen Harrow</strong>Director</div>
      <div class="team-photo" role="img" aria-label="Portrait of a director"></div>
      <div class="team-card gold"><strong>Tarek Saleh</strong>Director</div>
      <div class="team-card gold"><strong>Jo Ferrell</strong>Director</div>
      <div class="team-photo" role="img" aria-label="Portrait of a director"></div>
      <div class="team-card navy"><strong>Ava Lindqvist</strong>Senior Manager</div>
      <div class="team-photo" role="img" aria-label="Portrait of a manager"></div>
      <div class="team-photo" role="img" aria-label="Portrait of a manager"></div>
      <div class="team-card gold"><strong>Liam Chen</strong>Tax Manager</div>
      <div class="team-photo" role="img" aria-label="Portrait of an accountant"></div>
      <div class="team-card navy"><strong>Mia Ross</strong>Accountant</div>
    </div>
    <div class="photo tower-photo" role="img" aria-label="Photo of tall office towers seen from below"></div>
  </section>
</div>

<!-- Spread 2: Proposal / Letter -->
<div class="spread spread-2">
  <section class="page">
    <div class="page-bar"></div>
    <h2 class="proposal-heading">PROPOSAL FOR<br>OUTSOURCED CFO<br>SERVICES ADVISORY</h2>
    <div class="body-text prepared">
      <p><b>Prepared for:</b> Client Name, Company Pty Ltd<br><b>Prepared by:</b> Owen Harrow, Director, Thornvale Advisory</p>
    </div>
    <div class="bio bio-1">
      <div class="bio-photo" role="img" aria-label="Portrait of Owen Harrow"></div>
      <div class="bio-caption">Owen Harrow<br>Director</div>
      <div class="body-text bio-text">
        <p><b>Owen Harrow, CA, CTA, Director</b></p>
        <p>Owen has more than twenty years of experience in public practice and commercial finance. He leads our advisory work and acts as outsourced CFO for growing businesses.</p>
        <p>He works closely with owners on budgets, cash flow, funding and long-term planning, helping them turn their results into clear decisions.</p>
      </div>
    </div>
    <div class="bio bio-2">
      <div class="bio-photo" role="img" aria-label="Portrait of Jo Ferrell"></div>
      <div class="bio-caption">Jo Ferrell<br>Director</div>
      <div class="body-text bio-text">
        <p><b>Jo Ferrell, CA, Director – Financial Reporting and CFO Services</b></p>
        <p>Jo oversees financial reporting and management accounts for our CFO clients, with a strong focus on accuracy and timely delivery.</p>
        <p>She brings practical systems knowledge and helps teams improve their processes and reporting.</p>
      </div>
    </div>
  </section>
  <section class="page letter">
    <div class="page-bar"></div>
    <div class="logo">thornvale<span>advisory</span></div>
    <div class="body-text letter-text">
      <p>7 January 2025</p>
      <p>Client Name<br>Company Pty Ltd</p>
      <p><b>Engagement for Outsourced CFO Services</b></p>
      <p>Dear Client,</p>
      <p>Thank you for the opportunity to present this proposal. We have outlined below the services we recommend, based on our recent discussion.</p>
      <p>Our outsourced CFO service will include:</p>
      <p>• Monthly management reports and review of key results<br>• Cash flow forecasting and budget preparation<br>• Guidance on pricing, margins and cost control<br>• Support with banks, funding and investor reporting<br>• Quarterly strategy meetings with the directors</p>
      <p>Our team will also be available between meetings to answer questions and assist with any matters that arise during the year.</p>
      <p><b>Our approach</b></p>
      <p>We begin with a review of your current reporting and systems, then agree a calendar of deliverables that suits your business.</p>
      <p>We look forward to working with you.</p>
      <p>Kind regards,<br>Owen Harrow<br>Director</p>
    </div>
  </section>
</div>

<!-- Spread 3: Fees / Closing -->
<div class="spread spread-3">
  <section class="page">
    <div class="page-bar"></div>
    <table class="fee-table fees-1">
      <tr><th>Service</th><th>Frequency</th><th class="num">Fee (ex GST)</th></tr>
      <tr><td>Management reports</td><td>Monthly</td><td class="num">$1,200</td></tr>
      <tr><td>Cash flow forecast</td><td>Quarterly</td><td class="num">$1,800</td></tr>
      <tr><td>Budget preparation</td><td>Annual</td><td class="num">$2,500</td></tr>
      <tr><td>Strategy meetings</td><td>Quarterly</td><td class="num">$1,500</td></tr>
      <tr><td>Bank and funding support</td><td>As required</td><td class="num">$950</td></tr>
      <tr class="total"><td>Total annual fee</td><td></td><td class="num">$29,450</td></tr>
    </table>
    <div class="body-text fees-note">
      <p>Fees are based on the scope set out above and will be billed monthly in arrears. Any work outside this scope will be agreed with you before it begins.</p>
      <p>We review our fees each year and will give you notice of any change. All fees exclude GST and disbursements.</p>
      <p><b>Optional services</b></p>
    </div>
    <table class="fee-table fees-2">
      <tr><th>Optional service</th><th class="num">Fee (ex GST)</th></tr>
      <tr><td>Annual tax return</td><td class="num">$3,200</td></tr>
      <tr><td>BAS preparation</td><td class="num">$450</td></tr>
      <tr><td>Payroll review</td><td class="num">$800</td></tr>
      <tr class="total"><td>Total optional</td><td class="num">$4,450</td></tr>
    </table>
    <div class="body-text fees-tail">
      <p>To accept this proposal, please sign and return the enclosed engagement letter.</p>
    </div>
  </section>
  <section class="page">
    <div class="page-bar"></div>
    <div class="body-text close-text">
      <p>Should you have any questions, please contact Owen Harrow on 02 9000 0000 or visit www.thornvale.net.au.</p>
      <p>We look forward to a long and rewarding relationship with your business.</p>
    </div>
    <svg class="panels" width="360" height="500" viewBox="0 0 360 500" role="img" aria-label="Slanted photo panels of glass towers and a businesswoman on a phone">
      <defs>
        <linearGradient id="glass" x1="0" y1="0" x2="1" y2="1">
          <stop offset="0" stop-color="#0a2146"/>
          <stop offset=".5" stop-color="#3f74ad"/>
          <stop offset="1" stop-color="#0b1f3e"/>
        </linearGradient>
        <linearGradient id="glass-light" x1="0" y1="0" x2="0" y2="1">
          <stop offset="0" stop-color="#8fb0d3"/>
          <stop offset="1" stop-color="#1e4574"/>
        </linearGradient>
      </defs>
      <polygon points="20,80 90,40 90,470 20,500" fill="url(#glass-light)"/>
      <polygon points="100,36 200,0 200,440 100,466" fill="url(#glass)"/>
      <polygon points="210,0 290,30 290,420 210,440" fill="url(#glass-light)"/>
      <polygon points="300,34 360,56 360,400 300,416" fill="url(#glass)"/>
    </svg>
  </section>
</div>

</body>
</html>
```